Business card templates for our website plus designer opportunity

we require 100 business card designs to start with in the following categories (see below ) please note we require 1000`s of designs in all types of different fields this is just a tester to check the response , we are currently setting up a cardloom / printova type website/ marketplace we are now looking for freelance designers to make us some default designs to launch the site.

http://www.kelvoriq.example/

Brief about kelvoriq

we our a manufacture of a large range of products covering many industries we our currently setting up a marketplace where people can buy sell create and find personalized products and custom merchandised very much like printova and mugharbor we are now at the stage of adding content to the site for its launch we our currently looking for some core design templates in fact we need a lot of designs and we are currently looking for high quality designers to join our freelance design team .

The business cards designs

Please note all the text and data on the card can be the same so set up a default template to save yourself time all we really want is the core design front and back please , use cardloom printova mug harbor for reference or ideas please make sure they are not copied and we have full rights to the any copyright your design may contain , if we pick your designs you we will paid for them asked to make another 200 designs and you will be asked if you would like to join our freelance kelvoriq core design team you can always say no its perfectly fine but we have a lot of work to be designed for a lot of different products so there is a good opportunity here to get in before the site goes live in the next few months

Also note the chosen designs must be in vector format as well as jpeg and pdf , any vector files must be created to outlines
once we buy the designs we will own full rights to the copyright of said design and we can change and use these designs in anyway we see fit

Industry: ( 20 number designs for each ) Test run to check response

Agriculture & Farming
Animals & Pet Care
Art & Entertainment
Automotive & Transportation
Beauty & Spa

```html
<!DOCTYPE html>
<html lang="en">
<head>
<meta charset="utf-8">
<title>Dog Minding Business Card – Front and Back</title>
<link rel="stylesheet" href="https://fonts.googleapis.com/css2?family=Great+Vibes&family=Comfortaa:wght@700&family=Open+Sans:wght@400&display=swap">
<style>
  :root {
    --page-bg: #efe9e1;
    --card-white: #ffffff;
    --warm-cream: #fdf3ea;
    --orange: #f68b1f;
    --orange-deep: #ef7d12;
    --peach: #fcd3ab;
    --green-light: #c4e07a;
    --green: #98c93c;
    --tagline-green: #4d6a27;
    --ink: #1a1a1a;
    --icon-brown: #a4541c;
    --pup-light: #f6e6c6;
    --pup-mid: #e6c48e;
  }
  * { margin: 0; padding: 0; box-sizing: border-box; }
  html, body { width: 1000px; height: 1200px; overflow: hidden; }
  body { background: var(--page-bg); position: relative; }

  .card {
    position: absolute;
    left: 90px;
    width: 824px;
    height: 508px;
    overflow: hidden;
    box-shadow: 0 6px 18px rgba(0,0,0,0.25);
  }
  .card--front { top: 60px; background: var(--card-white); }
  .card--back { top: 627px; height: 507px; background: var(--orange); }
  .card svg.card-art { position: absolute; inset: 0; }

  .owner-name {
    position: absolute;
    font-family: "Great Vibes", cursive;
    font-weight: 400;
    line-height: 1;
    white-space: nowrap;
  }
  .card--front .owner-name {
    left: 56px; top: 44px;
    font-size: 68px;
    color: var(--ink);
  }
  .card--back .owner-name {
    left: 0; right: 0; top: 402px;
    text-align: center;
    font-size: 70px;
    color: var(--card-white);
  }

  .services {
    position: absolute;
    left: 110px; top: 126px;
    width: 344px;
    text-align: center;
    list-style: none;
    font-family: "Comfortaa", sans-serif;
    font-weight: 700;
    font-size: 19px;
    line-height: 33px;
    color: var(--tagline-green);
  }

  .contacts {
    position: absolute;
    left: 48px; top: 298px;
    list-style: none;
    font-family: "Open Sans", sans-serif;
    font-size: 20px;
    line-height: 37px;
    color: var(--ink);
  }
  .contacts li { display: flex; align-items: center; gap: 12px; }
  .contacts svg { width: 22px; height: 22px; flex: none; }
</style>
</head>
<body>

  <section class="card card--front">
    <svg class="card-art" viewBox="0 0 824 508" width="824" height="508">
      <defs>
        <linearGradient id="green-field" x1="1" y1="0" x2="0.3" y2="1">
          <stop offset="0" stop-color="var(--green-light)"/>
          <stop offset="1" stop-color="var(--green)"/>
        </linearGradient>
        <linearGradient id="white-field" x1="0" y1="0" x2="1" y2="0.6">
          <stop offset="0" stop-color="var(--card-white)"/>
          <stop offset="1" stop-color="var(--warm-cream)"/>
        </linearGradient>
        <radialGradient id="pup-tone" cx="0.5" cy="0.45" r="0.6">
          <stop offset="0" stop-color="var(--pup-light)"/>
          <stop offset="1" stop-color="var(--pup-mid)"/>
        </radialGradient>
      </defs>
      <rect class="base-field" width="824" height="508" fill="url(#white-field)"/>
      <path class="green-field" d="M632 0 L824 0 L824 508 L365 508 Q585 360 632 0 Z" fill="url(#green-field)"/>
      <path class="peach-band" d="M175 508 Q548 448 620 0 L640 0 Q600 410 365 508 Z" fill="var(--peach)"/>
      <path class="orange-band" d="M0 508 Q470 440 585 0 L622 0 Q560 452 175 508 Z" fill="var(--orange)"/>
      <rect class="puppy-photo" x="510" y="38" width="300" height="458" rx="130" fill="url(#pup-tone)"
            role="img" aria-label="Photo of a smiling golden retriever puppy sitting"/>
    </svg>

    <h1 class="owner-name">Your Name Here</h1>

    <ul class="services">
      <li>Dog minding service</li>
      <li>canine myofunctional therapist</li>
      <li>animal lover</li>
    </ul>

    <ul class="contacts">
      <li>
        <svg viewBox="0 0 22 22" aria-hidden="true">
          <rect x="2" y="5" width="18" height="12" fill="var(--icon-brown)"/>
          <path d="M2.5 5.5 L11 12 L19.5 5.5" fill="none" stroke="#fff" stroke-width="1.5"/>
          <path d="M2.5 16.5 L8.5 11 M19.5 16.5 L13.5 11" stroke="#fff" stroke-width="1.2"/>
        </svg>
        <span>hello@pawkeeper.example</span>
      </li>
      <li>
        <svg viewBox="0 0 22 22" aria-hidden="true">
          <path d="M2 8 Q11 1 20 8 L17 10 L15 7 Q11 5.5 7 7 L5 10 Z" fill="var(--icon-brown)"/>
          <path d="M6 10 L16 10 L19 19 L3 19 Z" fill="var(--icon-brown)"/>
          <circle cx="11" cy="14.5" r="2.4" fill="#fff"/>
        </svg>
        <span>055-010-2468-100</span>
      </li>
      <li>
        <svg viewBox="0 0 22 22" aria-hidden="true">
          <path d="M2 8 Q11 1 20 8 L17 10 L15 7 Q11 5.5 7 7 L5 10 Z" fill="var(--icon-brown)"/>
          <path d="M6 10 L16 10 L19 19 L3 19 Z" fill="var(--icon-brown)"/>
          <circle cx="11" cy="14.5" r="2.4" fill="#fff"/>
        </svg>
        <span>099-010-1357-200</span>
      </li>
    </ul>
  </section>

  <section class="card card--back">
    <svg class="card-art" viewBox="0 0 824 507" width="824" height="507">
      <defs>
        <radialGradient id="halo" cx="0.5" cy="0.5" r="0.5">
          <stop offset="0.8" stop-color="#fff" stop-opacity="0.55"/>
          <stop offset="1" stop-color="#fff" stop-opacity="0"/>
        </radialGradient>
        <radialGradient id="pup-tone-back" cx="0.5" cy="0.45" r="0.55">
          <stop offset="0" stop-color="var(--pup-light)"/>
          <stop offset="0.75" stop-color="var(--pup-mid)"/>
          <stop offset="1" stop-color="#ffffff"/>
        </radialGradient>
      </defs>
      <circle class="portrait-halo" cx="424" cy="202" r="182" fill="url(#halo)"/>
      <circle class="portrait-frame" cx="424" cy="202" r="160" fill="var(--card-white)" stroke="var(--orange-deep)" stroke-width="3"/>
      <circle class="puppy-portrait" cx="424" cy="202" r="156" fill="url(#pup-tone-back)"
              role="img" aria-label="Portrait photo of a smiling golden retriever puppy"/>
    </svg>

    <h2 class="owner-name">Your Name Here</h2>
  </section>

</body>
</html>
```